Velvet Bloom Marisol's Cleaning Service Business Cards Project

A business card with all contact details with logo design on there (already have a logo) eye catching Logo and contact info on one side, full logo on the back, must target upper class residential and corporate companies, fitness companies, still keep it on the feminine side of things , must look elegant

Target Market(s)

Upper class homes and corporate companies

Industry/Entity Type

Cleaning Service

Contact Information for Business Card

Name: Marisol Denhart
Position: Director
ABN: 47193062857
Email: marisolsvelvetcleaning@brightmail.example
Number: 0418926547

Font styles to use
Decorative

Colors

Designer to choose colors to be used in the design.

Requirements
Must have
• Available Sydney Wide, contact info and logo on one side, full logo on the back
Nice to have
• Professional appearance
Should not have
• Cheap advert looking stuff

```html
<!DOCTYPE html>
<html lang="en">
<head>
<meta charset="utf-8">
<title>Velvet Bloom – Business Cards</title>
<link href="https://fonts.googleapis.com/css2?family=Roboto:wght@300;400&display=swap" rel="stylesheet">
<style>
  :root {
    --backdrop: #262627;
    --card: #1a1a1b;
    --card-edge: #232324;
    --silver: #dcdcdc;
    --silver-muted: #a4a4a4;
    --rule: #6e6e6e;
  }
  * { box-sizing: border-box; margin: 0; padding: 0; }
  html, body { width: 1200px; height: 900px; overflow: hidden; }
  body {
    background: var(--backdrop);
    font-family: "Roboto", Arial, sans-serif;
    color: var(--silver);
    position: relative;
  }
  .card {
    position: absolute;
    left: 270px;
    width: 660px;
    height: 377px;
    background: linear-gradient(135deg, var(--card-edge), var(--card));
    box-shadow: 0 10px 30px rgba(0,0,0,0.45);
  }
  .card--front { top: 48px; }
  .card--back { top: 470px; }

  .brand {
    position: absolute;
    display: flex;
    flex-direction: column;
    align-items: center;
    text-align: center;
    font-weight: 300;
    letter-spacing: 0.12em;
    text-transform: uppercase;
  }
  .brand__dot {
    flex: none;
    border-radius: 50%;
  }

  .card--front .brand {
    left: 0; right: 0; top: 78px;
    gap: 26px;
    font-size: 24px;
    color: var(--silver);
  }
  .card--front .brand__dot {
    width: 96px; height: 96px;
    border: 1.5px solid var(--silver);
  }
  .card--front .brand__name { max-width: 460px; line-height: 1.5; }

  .card--back .brand {
    left: 24px; top: 92px;
    width: 230px;
    gap: 18px;
    font-size: 14px;
    color: var(--silver-muted);
  }
  .card--back .brand__dot {
    width: 70px; height: 70px;
    border: 1px solid var(--silver-muted);
  }
  .card--back .brand__name { line-height: 1.55; }

  .divider {
    position: absolute;
    left: 272px; top: 78px;
    width: 1px; height: 220px;
    background: var(--rule);
  }
  .contact {
    position: absolute;
    left: 300px; top: 88px;
  }
  .contact__name {
    font-size: 30px;
    font-weight: 400;
    letter-spacing: 0.03em;
    text-transform: uppercase;
    color: var(--silver);
  }
  .contact__role {
    font-size: 15px;
    color: var(--silver-muted);
    margin-top: 2px;
  }
  .contact__list { list-style: none; margin-top: 24px; }
  .contact__item {
    display: flex;
    align-items: center;
    gap: 10px;
    font-size: 15px;
    color: var(--silver);
    margin-bottom: 10px;
  }
  .contact__icon { width: 14px; height: 14px; flex: none; }
</style>
</head>
<body>
  <section class="card card--front" aria-label="Card front">
    <div class="brand">
      <span class="brand__dot"></span>
      <span class="brand__name">Velvet Bloom Marisol's Cleaning Service</span>
    </div>
  </section>

  <section class="card card--back" aria-label="Card back">
    <div class="brand">
      <span class="brand__dot"></span>
      <span class="brand__name">Velvet Bloom Marisol's Cleaning Service</span>
    </div>
    <div class="divider"></div>
    <div class="contact">
      <h1 class="contact__name">Marisol Denhart</h1>
      <p class="contact__role">Director</p>
      <ul class="contact__list">
        <li class="contact__item">ABN: 47193062857</li>
        <li class="contact__item">
          <svg class="contact__icon" viewBox="0 0 24 24" aria-hidden="true"><path fill="var(--silver)" d="M6.6 10.8a15.1 15.1 0 0 0 6.6 6.6l2.2-2.2c.3-.3.7-.4 1-.2 1.1.4 2.3.6 3.6.6.6 0 1 .4 1 1V20c0 .6-.4 1-1 1A17 17 0 0 1 3 4c0-.6.4-1 1-1h3.5c.6 0 1 .4 1 1 0 1.3.2 2.5.6 3.6.1.3 0 .7-.2 1l-2.3 2.2z"/></svg>
          0418926547
        </li>
        <li class="contact__item">
          <svg class="contact__icon" viewBox="0 0 24 24" aria-hidden="true"><rect x="3" y="5" width="18" height="14" rx="1.5" fill="none" stroke="var(--silver)" stroke-width="2"/><path d="M3 6l9 7 9-7" fill="none" stroke="var(--silver)" stroke-width="2"/></svg>
          marisolsvelvetcleaning@brightmail.example
        </li>
      </ul>
    </div>
  </section>
</body>
</html>
```